Product Description page for Hullwrap.com, References here just need a clean up redesign

Hi, were working on updating the product description page of our site hullwrap.com

Attached is a reference of what we drew on paint. We want to keep it pretty much the same as far as whats on there, the components with a few small adjustments and a clean actually designed look.

1. We want to remove the tabs (product description, warranty, reviews) and put it all in that main content area stretching down into sections. IE: Product Description section, followed by reviews, followed by warranty, below each other.
2. The side bar needs to be redesigned as far as the look and feel but the content and whats in there should stay the same.
3. The main banner area will be replaced shortly you do not have to worry about that.
4. Include a section or box for people to put in their email for a free Ebook.

Target Market(s)

people looking to easily view our boat cover products and buy without having to click too often or leave the page.

Industry/Entity Type

Online Shopping

Number of Pages Required

1 page

Requirements
Must have
• - Must update the sidebar
• - Must update the content area to remove the tabs and put the content from each tab sectioned off below each other (dummy text is fine for now for the tabs you cant view)
Nice to have
• - Cool place thats clean and functional to insert a section for people to put in their email to receive a free ebook
Should not have
• - too much change, we already know what we want and have a solid reference to work from.

```html
<!DOCTYPE html>
<html lang="en">
<head>
<meta charset="utf-8">
<title>Hullwrap.com – Product Page</title>
<link href="https://fonts.googleapis.com/css2?family=Arimo:wght@400;700&display=swap" rel="stylesheet">
<style>
:root{
  --brand-blue:#1d6cc9;
  --ink:#222;
  --muted:#666;
  --rule:#dcdcdc;
  --dark-bar:#333333;
  --sale-red:#e6411c;
  --orange:#e0562a;
  --orange-hi:#ff7d0a;
  --orange-lo:#e65100;
  --star:#f0a020;
  --green:#8cc21e;
  --green-lo:#6fa312;
  --footer-blue:#1e4fa6;
  --footer-navy:#132f86;
  --page:#ffffff;
  --soft:#f1f2f4;
}
*{box-sizing:border-box;margin:0;padding:0}
html,body{width:777px;height:1200px;overflow:hidden}
body{position:relative;background:var(--page);font-family:"Arimo",Arial,sans-serif;color:var(--ink)}
.abs{position:absolute}

/* header */
.brand{left:100px;top:10px;display:flex;align-items:center;gap:8px}
.brand-dot{width:22px;height:22px;border-radius:50%;background:var(--brand-blue)}
.brand-name{font-size:25px;font-weight:700;color:var(--brand-blue);letter-spacing:.2px}
.phone{right:99px;top:9px;text-align:right}
.phone-num{display:flex;align-items:center;gap:6px;justify-content:flex-end;font-size:16px;font-weight:700;color:var(--brand-blue)}
.phone-hours{font-size:7px;color:var(--muted);margin-top:2px}

.nav{left:0;top:48px;width:777px;height:23px;background:linear-gradient(#fbfbfb,#ececec);border-top:1px solid #ddd;border-bottom:1px solid #d0d0d0}
.nav-item{position:absolute;top:6px;font-size:9.5px;color:#333}
.nav-sep{position:absolute;top:5px;width:1px;height:13px;background:#d2d2d2}
.checkout{left:562px;top:47px;width:116px;height:21px;background:linear-gradient(#2f7fd8,#1a5fb8);color:#fff;font-size:7.5px;font-weight:700;display:flex;align-items:center;justify-content:center;gap:5px;border-radius:2px}
.checkout span{font-weight:400}

.crumbs{left:0;top:72px;width:777px;height:25px;background:var(--dark-bar)}
.crumbs ol{position:absolute;left:112px;top:8px;list-style:none;display:flex;gap:6px;font-size:7.5px;color:#bbb}
.crumbs li.cur{color:#fff}
.crumbs .sep{color:#aaa}

/* main card */
.card{left:102px;top:97px;width:576px;height:801px;background:#fff;box-shadow:0 1px 4px rgba(0,0,0,.25)}

.hero-photo{left:108px;top:108px;width:356px;height:180px;background:radial-gradient(ellipse at 55% 45%,#3e4fa6 0 28%,#d8dbe2 29% 45%,#fff 70%)}
.thumb{top:312px;width:46px;height:46px;border:1px solid #ccc}
.t1{left:134px;background:linear-gradient(#fff,#c9c9c9)}
.t2{left:196px;background:linear-gradient(#2d5fa8,#5b8ed0)}
.t3{left:257px;background:linear-gradient(135deg,#bfbfbf,#444)}
.t4{left:318px;background:linear-gradient(#d0d0d0,#333 60%,#bbb)}
.t5{left:379px;background:linear-gradient(135deg,#888,#111)}
.arrow{top:328px;font-size:11px;color:#bbb}

.sec-title{font-size:10px;font-weight:700;color:#222}
.copy{font-size:7.5px;line-height:9.6px;color:#333;width:350px}
.features{left:116px;top:494px;list-style:none;width:350px}
.features li{font-size:7.5px;height:28px;padding-left:12px;position:relative;color:#333}
.features li::before{content:"";position:absolute;left:1px;top:3px;width:3px;height:3px;border-radius:50%;background:#444}

/* buy box */
.prod-title{left:482px;top:110px;font-size:14.5px;line-height:18px;font-weight:700;color:#333;width:180px}
.stars{color:var(--star);font-size:9px;letter-spacing:.5px}
.rating-count{color:var(--sale-red);font-weight:700;font-size:9px}
.old-price{left:482px;top:172px;font-size:8.5px;color:#999;text-decoration:line-through;font-weight:700}
.on-sale{left:482px;top:187px;font-size:9px;font-weight:700;color:#222}
.on-sale em{font-style:normal;font-weight:400;color:var(--sale-red)}
.price{left:482px;top:202px;font-size:15px;font-weight:700;color:var(--sale-red)}
.opt-label{font-size:7.5px;color:#333}
.select{height:14px;border:1px solid #bbb;font-size:7.5px;color:#333;padding:2px 4px;display:flex;justify-content:space-between;align-items:center;background:#fff}
.swatch{top:235px;width:12px;height:12px}
.buy-rule{left:482px;top:279px;width:182px;height:1px;background:var(--rule)}
.addons{left:484px;top:289px;width:170px;list-style:none}
.addons li{display:flex;align-items:center;height:14px;font-size:7.5px;color:#222}
.addons .box{width:8px;height:8px;border:1px solid #999;border-radius:2px;margin-right:8px}
.addons .amt{margin-left:auto;color:var(--sale-red)}
.add-cart{left:486px;top:353px;width:179px;height:22px;background:linear-gradient(var(--orange-hi),var(--orange-lo));color:#fff;font-size:13px;display:flex;align-items:center;justify-content:center;letter-spacing:.3px}
.free-ship{left:486px;top:382px;width:179px;text-align:center;font-size:8px;font-style:italic;color:#4a8b1a;display:flex;justify-content:center;align-items:center;gap:3px}

.also-like{left:486px;top:429px;width:178px;height:25px;background:var(--dark-bar);color:#fff;font-size:9.5px;font-weight:700;display:flex;align-items:center;justify-content:center}
.rec{left:486px;width:178px;border:1px solid #e2e2e2;box-shadow:0 1px 2px rgba(0,0,0,.15);background:#fff}
.rec-photo{position:absolute;left:10px;top:8px;width:158px;height:72px}
.rec-name{position:absolute;left:0;top:92px;width:100%;text-align:center;font-size:7.5px;line-height:9.6px;color:#222;padding:0 10px}
.rec-band{position:absolute;left:0;top:118px;width:100%;height:22px;background:var(--orange);color:#fff;font-weight:700;font-size:9.5px;display:flex;align-items:center;justify-content:center}
.rec-meta{position:absolute;left:8px;top:148px;font-size:7.5px;line-height:12.5px;color:#222}
.rec-meta .fs{color:var(--sale-red)}
.rec-meta .stars{font-size:10px;color:var(--sale-red);margin:0 4px}

/* newsletter */
.nl-title{left:102px;top:934px;font-size:15px;font-weight:700;color:#1b76b9}
.nl-copy{left:102px;top:957px;font-size:7.5px;line-height:9.6px;color:#333;width:210px}
.nl-field{left:346px;top:930px;width:319px;height:40px;border-radius:20px;background:#e6e6e6;border:1px solid #cfcfcf;box-shadow:inset 0 1px 3px rgba(0,0,0,.15)}
.nl-field span{position:absolute;left:14px;top:12px;font-size:12px;font-style:italic;color:#9a9a9a}
.nl-btn{left:561px;top:933px;width:101px;height:34px;border-radius:17px;background:linear-gradient(#9bd22a,var(--green-lo));color:#fff;font-size:12.5px;font-weight:700;display:flex;align-items:center;justify-content:center}

/* footer */
.foot-strip{left:0;top:995px;width:777px;height:6px;background:var(--soft)}
.foot-scene{left:0;top:1001px;width:777px;height:199px;background:linear-gradient(#f3f6f8 0,#c9d4df 14%,#8fa3b9 26%,#4e6a58 42%,#3c5d8f 52%,#2f63b4 62%,var(--footer-navy) 100%)}
.foot-bar{left:98px;top:1118px;width:580px;height:26px;background:var(--footer-blue);border:1px solid #4c78c4;border-radius:2px}
.foot-bar .lead{position:absolute;left:14px;top:8px;font-size:7.5px;font-weight:700;color:#fff}
.foot-input{position:absolute;left:155px;top:6px;width:112px;height:13px;background:#fff}
.foot-sub{position:absolute;left:268px;top:6px;width:49px;height:13px;background:#f26b1d;color:#fff;font-size:6.5px;font-weight:700;display:flex;align-items:center;justify-content:center}
.foot-links{position:absolute;right:12px;top:8px;display:flex;gap:7px;font-size:7.5px;font-weight:700;color:#fff;text-decoration:underline}
.foot-rule{left:98px;top:1154px;width:580px;height:1px;background:#3f63b0}
.legal{left:0;top:1164px;width:777px;text-align:center;font-size:6.5px;line-height:8.8px;color:#7d93c8}
.legal u{color:#c9d6f2}
</style>
</head>
<body>

<header>
  <div class="abs brand"><span class="brand-dot"></span><span class="brand-name">Hullwrap.com</span></div>
  <div class="abs phone">
    <div class="phone-num">
      <svg width="15" height="11" viewBox="0 0 15 11"><path d="M1 4 Q7.5 -1 14 4 L12 5.5 L10 4 L10 3 Q7.5 2 5 3 L5 4 L3 5.5Z M3 6 H12 V10.5 H3Z" fill="var(--brand-blue)"/></svg>
      (800) 555-0147
    </div>
    <div class="phone-hours">Store Hours(M-F, 9:30AM - 6PM PST)</div>
  </div>
</header>

<nav class="abs nav">
  <span class="nav-item" style="left:112px">Boat Covers</span>
  <span class="nav-sep" style="left:178px"></span>
  <span class="nav-item" style="left:194px">Bass Boat Covers</span>
  <span class="nav-sep" style="left:285px"></span>
  <span class="nav-item" style="left:301px">T Top Boat Covers</span>
  <span class="nav-sep" style="left:396px"></span>
  <span class="nav-item" style="left:411px">Bimini Tops</span>
  <span class="nav-sep" style="left:477px"></span>
  <span class="nav-item" style="left:491px">Jet Ski Covers</span>
</nav>
<div class="abs checkout">
  <svg width="11" height="9" viewBox="0 0 11 9"><path d="M0 1 H2 L3.5 6 H9 L10.5 2 H3" fill="none" stroke="#fff" stroke-width="1.2"/><circle cx="4" cy="8" r="1" fill="#fff"/><circle cx="8.5" cy="8" r="1" fill="#fff"/></svg>
  CHECKOUT : <span>(0) Items</span> ▾
</div>

<div class="abs crumbs">
  <ol>
    <li>Home</li><li class="sep">›</li>
    <li>Boat Covers</li><li class="sep">›</li>
    <li>Runabout w</li><li class="sep">›</li>
    <li class="cur">up to 18'8" Wide</li>
  </ol>
</div>

<main>
  <div class="abs card"></div>

  <div class="abs hero-photo" role="img" aria-label="Runabout boat on a trailer wearing a navy blue fitted cover"></div>
  <span class="abs arrow" style="left:116px">‹</span>
  <div class="abs thumb t1" role="img" aria-label="Product quality badge thumbnail"></div>
  <div class="abs thumb t2" role="img" aria-label="Cover fabric detail thumbnail"></div>
  <div class="abs thumb t3" role="img" aria-label="Tie-down strap thumbnail"></div>
  <div class="abs thumb t4" role="img" aria-label="Buckle strap thumbnail"></div>
  <div class="abs thumb t5" role="img" aria-label="Strap clip thumbnail"></div>
  <span class="abs arrow" style="left:440px">›</span>

  <h2 class="abs sec-title" style="left:116px;top:396px">Description :</h2>
  <p class="abs copy" style="left:116px;top:413px">Maecenas id dictum risus. Pellentesque aliquam augue eget fringilla feugiat. In hendrerit, est sed faucibus eleifend, ligula quam varius sapien, a efficitur orci velit a tellus. Aenean faucibus aliquet lobortis. Ut sit amet elit ligula. Nunc sit amet luctus erat. Vestibulum urna nulla, laoreet nec tempus at, eleifend eu tellus. Nunc sit amet elit a risus iaculis consectetur non accumsan mauris.</p>

  <h2 class="abs sec-title" style="left:116px;top:477px">Features :</h2>
  <ul class="abs features">
    <li>Maecenas id dictum risus. Pellentesque aliquam</li>
    <li>augue eget fringilla feugiat. In hendrerit, est sed</li>
    <li>faucibus eleifend, ligula quam varius sapien,</li>
    <li>Aenean faucibus aliquet lobortis.</li>
    <li>Ut sit amet elit ligula. Nunc sit amet luctus erat.</li>
    <li>Vestibulum urna nulla, laoreet nec tempus at,</li>
    <li>eleifend eu tellus. Nunc sit amet elit a risus iaculis</li>
    <li>consectetur non accumsan mauris.</li>
  </ul>

  <h2 class="abs sec-title" style="left:116px;top:716px">Description :</h2>
  <p class="abs copy" style="left:116px;top:733px">Maecenas id dictum risus. Pellentesque aliquam augue eget fringilla feugiat. In hendrerit, est sed faucibus eleifend, ligula quam varius sapien, a efficitur orci velit a tellus. Aenean faucibus aliquet lobortis. Ut sit amet elit ligula. Nunc sit amet luctus erat.</p>
  <p class="abs copy" style="left:116px;top:772px">Vestibulum urna nulla, laoreet nec tempus at, eleifend eu tellus. Nunc sit amet elit a risus iaculis consectetur non accumsan mauris.</p>
  <p class="abs copy" style="left:116px;top:801px">Lorem ipsum dolor sit amet, consectetur adipiscing elit. Pellentesque ligula dui, condimentum sit amet scelerisque eu, sodales vitae sem. Aenean tincidunt, neque at imperdiet sodales, elit libero maximus nisl, a pharetra ipsum nulla quis risus. Nam tincidunt felis felis, rutrum pharetra ante ultrices a. Nullam ut sapien ut sapien faucibus fermentum. Praesent et eros porta, iaculis libero ac, lacinia purus. Sed sagittis eget erat in bibendum. Aliquam a est dolor. Praesent convallis commodo est, quis fringilla tortor tincidunt eget. Suspendisse eu mollis tortor. Nunc faucibus nulla ac lorem ultrices interdum. Curabitur vel nibh ac arcu auctor tincidunt ut ac ante. Fusce molestie nec erat ac scelerisque.</p>

  <!-- buy box -->
  <h1 class="abs prod-title">Lorem ipsum dolor sit amet cover</h1>
  <div class="abs" style="left:482px;top:153px"><span class="stars">★★★★☆</span> <span class="rating-count">(1,471)</span></div>
  <div class="abs old-price">$248.00</div>
  <div class="abs on-sale">On Sale : <em>10% Off</em></div>
  <div class="abs price">$223.20</div>

  <span class="abs opt-label" style="left:483px;top:237px">Color &nbsp;:</span>
  <div class="abs select" style="left:515px;top:234px;width:88px">Choose an optiuon <span>▼</span></div>
  <span class="abs swatch" style="left:609px;background:#1a7bd0"></span>
  <span class="abs swatch" style="left:625px;background:#7f7f7f"></span>

  <span class="abs opt-label" style="left:483px;top:259px">Quantity &nbsp;:</span>
  <div class="abs select" style="left:526px;top:256px;width:27px">1 <span>▼</span></div>

  <div class="abs buy-rule"></div>
  <ul class="abs addons">
    <li><span class="box"></span>ellentesque ligula dui condim<span class="amt">$25.00</span></li>
    <li><span class="box"></span>sit amet scelerisque eu, sodales<span class="amt">$30.00</span></li>
    <li><span class="box"></span>Aenean tincidunt, neque at<span class="amt">$11.00</span></li>
    <li><span class="box"></span>imperdiet sodales, elit libero<span class="amt">$21.00</span></li>
  </ul>
  <div class="abs add-cart">ADD TO CART</div>
  <div class="abs free-ship">
    <svg width="9" height="7" viewBox="0 0 9 7"><path d="M0 0 H5.5 V5 H0Z M5.5 1.5 H7.5 L9 3.3 V5 H5.5Z" fill="#4a8b1a"/><circle cx="2" cy="6" r="1" fill="#4a8b1a"/><circle cx="7" cy="6" r="1" fill="#4a8b1a"/></svg>
    Free Shipping!
  </div>

  <aside>
    <div class="abs also-like">You may also like</div>

    <div class="abs rec" style="top:472px;height:196px">
      <div class="rec-photo" role="img" aria-label="Boat on trailer with a grey fitted cover" style="background:radial-gradient(ellipse at 50% 45%,#59636f 0 30%,#dfe2e6 31% 50%,#fff 72%)"></div>
      <p class="rec-name">Lorem ipsum dolor sit amet, consectetur adipiscing elit.</p>
      <div class="rec-band">ON SALE</div>
      <div class="rec-meta">From &nbsp;: &nbsp;$152.30<br><span class="fs">Free Shipping</span><br>Rating <span class="stars">★★★★☆</span> (1k+)</div>
    </div>

    <div class="abs rec" style="top:682px;height:197px">
      <div class="rec-photo" role="img" aria-label="Tower boat on trailer with a red fitted cover" style="background:radial-gradient(ellipse at 50% 45%,#d8343c 0 30%,#e6e6e8 31% 50%,#fff 72%)"></div>
      <p class="rec-name">Lorem ipsum dolor sit amet, consectetur adipiscing elit.</p>
      <div class="rec-band">ON SALE</div>
      <div class="rec-meta">From &nbsp;: &nbsp;$152.30<br><span class="fs">Free Shipping</span><br>Rating <span class="stars">★★★★☆</span> (1k+)</div>
    </div>
  </aside>
</main>

<section>
  <h2 class="abs nl-title">Subscribe to our Newsletter</h2>
  <p class="abs nl-copy">Lorem ipsum dolor sit amet, consectetur adipiscing elit. Pellentesque ligula dui.</p>
  <div class="abs nl-field"><span>Enter Your Email</span></div>
  <div class="abs nl-btn">Sign Up</div>
</section>

<footer>
  <div class="abs foot-strip"></div>
  <div class="abs foot-scene" role="img" aria-label="Harbor with moored sailboats, wooded shoreline and misty mountains over blue water"></div>
  <div class="abs foot-bar">
    <span class="lead">Sign Up To Win A FREE Boat Cover!</span>
    <span class="foot-input"></span>
    <span class="foot-sub">Subscribe ›</span>
    <span class="foot-links"><span>Exchanges &amp; Returns</span><span>Contact Us</span></span>
  </div>
  <div class="abs foot-rule"></div>
  <div class="abs legal">Copyright © 2016 Hullwrap.com. All Rights Reserved<br>412 Harbor View Road, Port Dalton NY 10599<br><u>Privacy Policy</u></div>
</footer>

</body>
</html>
```